" Empresa de Advocacia composta de três sócios majoritários, quais sa: PAULO HENRIQUE AMARAL DE BRANDÃO; ROSANA BEATRIZ VILELA DE BRANDÃO; e, PAULO HENRIQUE VILELA DE BRANDÃO, escritório voltado para o DIREITO CIVIL - Em especial Família e Sucessoes "

```html
<!DOCTYPE html>
<html lang="pt-BR">
<head>
<meta charset="utf-8">
<title>Brandão &amp; Brandão – Cartão de Visita</title>
<link href="https://fonts.googleapis.com/css2?family=Cinzel:wght@400;500&family=Open+Sans:wght@400;600&display=swap" rel="stylesheet">
<style>
  :root {
    --stage: #8b8b8b;
    --plum-light: #4d2b43;
    --plum-dark: #1d0f19;
    --gold: #c89b2e;
    --gold-soft: #b8913f;
    --paper: #ffffff;
    --ink: #3a2c36;
    --ink-soft: #5a5a5a;
    --ghost: #ececec;
    --rule: #cfcfcf;
  }
  * { margin: 0; padding: 0; box-sizing: border-box; }
  html, body { width: 1200px; height: 1200px; overflow: hidden; }
  body { background: var(--stage); position: relative; font-family: "Open Sans", Arial, sans-serif; }

  .card {
    position: absolute;
    left: 228px;
    width: 756px;
    height: 415px;
    border-radius: 14px 56px 14px 56px;
    overflow: hidden;
  }
  .card--front {
    top: 168px;
    background: radial-gradient(ellipse at 45% 40%, var(--plum-light) 0%, var(--plum-dark) 85%);
  }
  .card--back { top: 617px; background: var(--paper); }

  .mark-disc { position: absolute; border-radius: 50%; }
  .card--front .mark-disc { left: 288px; top: 0; width: 0; }
  .front-disc { left: 60px; top: 0; width: 336px; height: 336px; top: 0; }

  .firm-name {
    position: absolute;
    font-family: "Cinzel", "Times New Roman", serif;
    font-weight: 500;
    white-space: nowrap;
  }
  .firm-tagline {
    position: absolute;
    font-family: "Cinzel", "Times New Roman", serif;
    white-space: nowrap;
    letter-spacing: 3px;
  }

  .card--front .firm-name { left: 374px; top: 310px; font-size: 33px; color: var(--gold); }
  .card--front .firm-rule { position: absolute; left: 390px; top: 352px; width: 300px; height: 1px; background: var(--gold-soft); opacity: .6; }
  .card--front .firm-tagline { left: 420px; top: 357px; font-size: 10px; color: var(--gold-soft); }

  .card--back .ghost-disc { left: 36px; top: -6px; width: 412px; height: 412px; border: 34px solid var(--ghost); }
  .card--back .small-disc { left: 197px; top: 115px; width: 54px; height: 54px; background: var(--gold); }
  .card--back .firm-name { left: 70px; top: 218px; width: 310px; text-align: center; font-size: 34px; color: var(--ink-soft); }
  .card--back .firm-tagline { left: 70px; top: 264px; width: 310px; text-align: center; font-size: 10px; color: var(--ink-soft); }

  .contact { position: absolute; left: 422px; top: 154px; width: 334px; color: var(--ink); }
  .contact__name { font-size: 17px; font-weight: 600; line-height: 22px; }
  .contact__role { font-size: 11px; letter-spacing: .5px; margin-top: 2px; color: var(--ink-soft); }
  .contact__rule { height: 1px; background: var(--rule); margin: 9px 0 14px; }
  .contact__list { list-style: none; font-size: 13px; line-height: 20px; color: var(--ink-soft); }
  .contact__list li { display: flex; align-items: flex-start; gap: 8px; margin-bottom: 6px; }
  .contact__list svg { width: 14px; height: 14px; margin-top: 3px; flex: none; fill: var(--ink); }
</style>
</head>
<body>

<section class="card card--front" aria-label="Frente do cartão">
  <div class="mark-disc front-disc" style="left:60px; top:40px; width:336px; height:336px; background: var(--gold);"></div>
  <div class="firm-name">BRANDÃO &amp; BRANDÃO</div>
  <div class="firm-rule"></div>
  <div class="firm-tagline">ADVOGADOS ASSOCIADOS</div>
</section>

<section class="card card--back" aria-label="Verso do cartão">
  <div class="mark-disc ghost-disc"></div>
  <div class="mark-disc small-disc"></div>
  <div class="firm-name" style="font-size:27px;">BRANDÃO &amp; BRANDÃO</div>
  <div class="firm-tagline">ADVOGADOS ASSOCIADOS</div>

  <div class="contact">
    <p class="contact__name">Rosana Beatriz Vilela de Brandão</p>
    <p class="contact__role">ADVOGADA</p>
    <div class="contact__rule"></div>
    <ul class="contact__list">
      <li>
        <svg viewBox="0 0 24 24" aria-hidden="true"><path d="M12 2a7 7 0 0 0-7 7c0 5 7 13 7 13s7-8 7-13a7 7 0 0 0-7-7zm0 9.5A2.5 2.5 0 1 1 12 6.5a2.5 2.5 0 0 1 0 5z"/></svg>
        <span>SHIS QL 14, Conj. 03, Casa 07<br>LAGO NORTE - CEP 71.500-120</span>
      </li>
      <li>
        <svg viewBox="0 0 24 24" aria-hidden="true"><path d="M2 5h20v14H2zM4 7v.4l8 5 8-5V7z"/></svg>
        <span>brandaoebrandao@exemplo.com.br</span>
      </li>
      <li>
        <svg viewBox="0 0 24 24" aria-hidden="true"><path d="M6.6 10.8a15 15 0 0 0 6.6 6.6l2.2-2.2a1 1 0 0 1 1-.25 11.4 11.4 0 0 0 3.6.57 1 1 0 0 1 1 1V20a1 1 0 0 1-1 1A17 17 0 0 1 3 4a1 1 0 0 1 1-1h3.5a1 1 0 0 1 1 1c0 1.25.2 2.45.57 3.57a1 1 0 0 1-.25 1z"/></svg>
        <span>(61) 3400.1234 / 9800.5678</span>
      </li>
    </ul>
  </div>
</section>

</body>
</html>
```